We are needing a bookcover for a reprint of our book "Whispers Beneath the Amber Horizon". It takes a look at the geologic formation found in the great plains. Our original cover was colorful and showed rock layers. Something similar but different and eye catching would be great. a geologic cross section showing various layers or possibly some different rocks/soils. We are really open to suggestions attached is the current book cover with the colored layers and the cover from the 80s.

Target Market(s)

Adult Readers

Industry/Entity Type

Nonprofit retail - science - nature

Requirements
Must have
• Geology or rock layers
Nice to have
• Books title, Geologic cross section
Should not have
• People or animals, no photos prefer sketch

```html
<!DOCTYPE html>
<html lang="en">
<head>
<meta charset="utf-8">
<title>Whispers Beneath the Amber Horizon — Cover</title>
<link rel="stylesheet" href="https://fonts.googleapis.com/css2?family=Alfa+Slab+One&display=swap">
<style>
  :root{
    --backdrop:#808184;
    --ink:#000000;
    --paper:#ffffff;
    --sky:#8fd3f1;
    --blue:#6aaed8;
    --deep-blue:#4a8ec8;
    --periwinkle:#92a9d8;
    --lavender:#d6dcef;
    --pale-lavender:#e2e6f3;
    --teal:#3f9fb0;
    --light-teal:#8cc8d8;
    --pink:#f6c3b5;
    --green:#5fa882;
    --peach:#fbc99b;
    --orange:#f8b98a;
    --yellow:#fde89c;
    --pale-yellow:#fdf0ae;
  }
  *{margin:0;padding:0;box-sizing:border-box}
  html,body{width:849px;height:1200px;overflow:hidden;background:var(--backdrop)}
  .cover{
    position:absolute;left:73px;top:73px;width:702px;height:1053px;
    box-shadow:6px 8px 14px rgba(0,0,0,.35);
    overflow:hidden;
  }
  .strata{position:absolute;inset:0;display:flex;flex-direction:column}
  .layer{width:100%}
  .layer.sky{background:var(--sky)}
  .layer.blue{background:var(--blue)}
  .layer.deep-blue{background:var(--deep-blue)}
  .layer.periwinkle{background:var(--periwinkle)}
  .layer.lavender{background:var(--lavender)}
  .layer.pale-lavender{background:var(--pale-lavender)}
  .layer.teal{background:var(--teal)}
  .layer.light-teal{background:var(--light-teal)}
  .layer.pink{background:var(--pink)}
  .layer.green{background:var(--green)}
  .layer.peach{background:var(--peach)}
  .layer.orange{background:var(--orange)}
  .layer.yellow{background:var(--yellow)}
  .layer.pale-yellow{background:var(--pale-yellow)}
  .layer.white{background:var(--paper);border-top:2px solid var(--ink);border-bottom:2px solid var(--ink)}
  .layer.black{background:var(--ink)}
  .layer.gradient-blue{background:linear-gradient(var(--light-teal),#e8f4f8 70%,var(--light-teal))}
  .layer.interfingering{
    background:linear-gradient(180deg,var(--yellow) 0%,var(--peach) 35%,var(--teal) 70%,var(--light-teal) 100%);
  }
  .title{position:absolute;left:0;top:0;width:702px;height:260px}
  .title text{font-family:"Alfa Slab One",serif;stroke:var(--ink);stroke-linejoin:round;paint-order:stroke}
  .title .shadow{fill:var(--ink);stroke:var(--ink)}
  .title .rule{fill:var(--paper);stroke:var(--ink);stroke-width:2}
</style>
</head>
<body>
<main class="cover">
  <div class="strata">
    <div class="layer blue" style="flex:35"></div>
    <div class="layer pink" style="flex:45"></div>
    <div class="layer green" style="flex:50"></div>
    <div class="layer peach" style="flex:15"></div>
    <div class="layer white" style="flex:50"></div>
    <div class="layer yellow" style="flex:20"></div>
    <div class="layer yellow" style="flex:45"></div>
    <div class="layer gradient-blue" style="flex:40"></div>
    <div class="layer pale-yellow" style="flex:20"></div>
    <div class="layer light-teal" style="flex:25"></div>
    <div class="layer periwinkle" style="flex:35"></div>
    <div class="layer periwinkle" style="flex:20"></div>
    <div class="layer periwinkle" style="flex:20"></div>
    <div class="layer black" style="flex:5"></div>
    <div class="layer teal" style="flex:15"></div>
    <div class="layer light-teal" style="flex:15"></div>
    <div class="layer deep-blue" style="flex:25"></div>
    <div class="layer black" style="flex:10"></div>
    <div class="layer orange" style="flex:10"></div>
    <div class="layer periwinkle" style="flex:20"></div>
    <div class="layer black" style="flex:10"></div>
    <div class="layer teal" style="flex:15"></div>
    <div class="layer blue" style="flex:10"></div>
    <div class="layer orange" style="flex:35"></div>
    <div class="layer black" style="flex:15"></div>
    <div class="layer light-teal" style="flex:10"></div>
    <div class="layer pale-yellow" style="flex:25"></div>
    <div class="layer blue" style="flex:25"></div>
    <div class="layer black" style="flex:10"></div>
    <div class="layer light-teal" style="flex:25"></div>
    <div class="layer peach" style="flex:15"></div>
    <div class="layer teal" style="flex:25"></div>
    <div class="layer black" style="flex:15"></div>
    <div class="layer yellow" style="flex:20"></div>
    <div class="layer interfingering" style="flex:85" role="img" aria-label="Interfingering sandstone and shale beds in a zigzag cross-section pattern"></div>
    <div class="layer black" style="flex:10"></div>
    <div class="layer light-teal" style="flex:30"></div>
    <div class="layer sky" style="flex:20"></div>
    <div class="layer yellow" style="flex:30"></div>
    <div class="layer teal" style="flex:25"></div>
    <div class="layer peach" style="flex:20"></div>
    <div class="layer sky" style="flex:40"></div>
    <div class="layer lavender" style="flex:15"></div>
    <div class="layer pale-lavender" style="flex:180"></div>
    <div class="layer white" style="flex:35"></div>
    <div class="layer sky" style="flex:85"></div>
  </div>

  <svg class="title" viewBox="0 0 702 260" aria-labelledby="book-title">
    <title id="book-title">Whispers Beneath the Amber Horizon</title>
    <g aria-hidden="true">
      <text class="shadow" x="40" y="100" font-size="80" stroke-width="6" textLength="624" lengthAdjust="spacingAndGlyphs">WHISPERS</text>
      <text class="shadow" x="141" y="150" font-size="44" stroke-width="5" textLength="428" lengthAdjust="spacingAndGlyphs">BENEATH THE</text>
      <text class="shadow" x="38" y="230" font-size="66" stroke-width="6" textLength="648" lengthAdjust="spacingAndGlyphs">AMBER HORIZON</text>
    </g>
    <rect class="rule" x="25" y="123" width="90" height="9"/>
    <rect class="rule" x="585" y="123" width="90" height="9"/>
    <text x="35" y="95" font-size="80" fill="var(--paper)" stroke-width="5" textLength="624" lengthAdjust="spacingAndGlyphs">WHISPERS</text>
    <text x="138" y="146" font-size="44" fill="var(--paper)" stroke-width="4" textLength="428" lengthAdjust="spacingAndGlyphs">BENEATH THE</text>
    <text x="33" y="225" font-size="66" stroke-width="5" textLength="648" lengthAdjust="spacingAndGlyphs"><tspan fill="var(--pale-yellow)">A</tspan><tspan fill="var(--light-teal)">M</tspan><tspan fill="var(--periwinkle)">B</tspan><tspan fill="var(--green)">E</tspan><tspan fill="var(--pink)">R</tspan><tspan fill="var(--paper)"> </tspan><tspan fill="var(--light-teal)">H</tspan><tspan fill="var(--sky)">O</tspan><tspan fill="var(--blue)">R</tspan><tspan fill="var(--peach)">I</tspan><tspan fill="var(--periwinkle)">Z</tspan><tspan fill="var(--light-teal)">O</tspan><tspan fill="var(--pale-yellow)">N</tspan></text>
  </svg>
</main>
</body>
</html>
```